Flyer Lieferservice / Gutschein / Visitenkarte
Zielgruppe
Restaurant
Aufgabenstellung
Wir benötigen:
Lieferservice Flyer mit Speisekarte
Gutschein Flyer
Visitenkarten
Farbe: Schwarz & Gold siehe Website
Speisekarte: (siehe Anhang)
Wichtige Inhalte:
Speiskarte
Social Media
Anschrift
Telefonnummer
Website
App Verweis
(bishergie Flyer zur Ansicht im Anhang)

```html
<!DOCTYPE html>
<html lang="de">
<head>
<meta charset="utf-8">
<title>Restaurant Zur Goldlinde – Visitenkarte</title>
<link rel="stylesheet" href="https://fonts.googleapis.com/css2?family=Righteous&display=swap">
<style>
  :root {
    --gold: #d4af37;
    --black: #000000;
  }
  html, body {
    margin: 0;
    padding: 0;
    width: 1200px;
    height: 686px;
    overflow: hidden;
    background: var(--black);
  }
  .card {
    position: relative;
    width: 1200px;
    height: 686px;
    box-sizing: border-box;
    border: 7px solid var(--gold);
    background: var(--black);
    overflow: hidden;
    font-family: "Righteous", "Arial Black", sans-serif;
    color: var(--gold);
  }
  .side-bar {
    position: absolute;
    left: 53px;
    top: -7px;
    width: 63px;
    height: 636px;
    background: var(--gold);
    border-radius: 0 0 32px 32px;
  }
  .corner-stripes {
    position: absolute;
    left: 0;
    top: 0;
    width: 1186px;
    height: 672px;
  }
  .brand-mark {
    position: absolute;
    left: 546px;
    top: 13px;
    width: 150px;
    height: 150px;
    box-sizing: border-box;
    border: 1.5px solid var(--gold);
    border-radius: 50%;
  }
  .brand-name {
    position: absolute;
    left: 0;
    right: 0;
    top: 178px;
    padding-left: 65px;
    text-align: center;
    font-size: 40px;
    letter-spacing: 1px;
    margin: 0;
    font-weight: 400;
  }
  .icon {
    position: absolute;
    width: 48px;
    height: 48px;
  }
  .icon-phone  { left: 59px; top: 303px; }
  .icon-web    { left: 61px; top: 373px; }
  .icon-pin    { left: 60px; top: 444px; }
  .icon-social { left: 59px; top: 511px; }
  .contact {
    position: absolute;
    left: 144px;
    margin: 0;
    white-space: nowrap;
    line-height: 1;
  }
  .phone   { top: 318px; font-size: 26px; letter-spacing: 6px; }
  .web     { top: 376px; font-size: 16px; letter-spacing: 5px; line-height: 19px; }
  .street  { top: 448px; font-size: 24px; letter-spacing: 6px; }
  .city    { top: 477px; font-size: 15px; letter-spacing: 5px; }
  .social  { top: 523px; font-size: 16px; letter-spacing: 5px; }
</style>
</head>
<body>
<main class="card">
  <div class="side-bar"></div>

  <svg class="corner-stripes" viewBox="0 0 1186 672" aria-hidden="true">
    <g stroke="var(--gold)" stroke-width="11" stroke-linecap="butt">
      <line x1="1195" y1="430" x2="950" y2="675"/>
      <line x1="1195" y1="520" x2="1040" y2="675"/>
      <line x1="1195" y1="590" x2="1110" y2="675"/>
    </g>
  </svg>

  <div class="brand-mark"></div>
  <h1 class="brand-name">Restaurant Zur Goldlinde</h1>

  <svg class="icon icon-phone" viewBox="0 0 48 48" aria-hidden="true">
    <path d="M4 14 C6 6 42 6 44 14 L44 19 L34 19 L33 15 C28 13 20 13 15 15 L14 19 L4 19 Z" fill="var(--black)"/>
    <path d="M11 36 L14 22 L34 22 L37 36 Z" fill="var(--black)"/>
    <circle cx="24" cy="28" r="5" fill="none" stroke="var(--gold)" stroke-width="1.5"/>
  </svg>

  <svg class="icon icon-web" viewBox="0 0 48 48" aria-hidden="true">
    <circle cx="24" cy="24" r="23" fill="var(--black)"/>
    <g fill="none" stroke="var(--gold)" stroke-width="2">
      <circle cx="24" cy="24" r="15"/>
      <ellipse cx="24" cy="24" rx="7" ry="15"/>
      <line x1="24" y1="9" x2="24" y2="39"/>
      <line x1="9" y1="24" x2="39" y2="24"/>
      <path d="M12 16 H36 M12 32 H36"/>
    </g>
  </svg>

  <svg class="icon icon-pin" viewBox="0 0 48 48" aria-hidden="true">
    <circle cx="24" cy="24" r="24" fill="var(--black)"/>
    <path d="M24 37 C18 29 14 24 14 19 A10 10 0 0 1 34 19 C34 24 30 29 24 37 Z" fill="var(--gold)"/>
    <circle cx="24" cy="19" r="4" fill="var(--black)"/>
  </svg>

  <svg class="icon icon-social" viewBox="0 0 48 48" aria-hidden="true">
    <circle cx="24" cy="24" r="23" fill="var(--black)"/>
  </svg>

  <p class="contact phone">07231/5520419</p>
  <p class="contact web">restaurantzurgoldlinde.de<br>info@restaurantzurgoldlinde.de</p>
  <p class="contact street">Lindenweg 14</p>
  <p class="contact city">76199 Kleinsteinach</p>
  <p class="contact social">social: @zurGoldlinde</p>
</main>
</body>
</html>
```